Training Materials Cover design

Graphic design for the front and back cover of a training manual. Review my website at www.vbtrelmo.com. The business name is Meridale Institute of Trade Vexmo

Target Market(s)

Professional people and those interested in professional and personal development

Requirements
Must have
• Front and back cover. Should include my current logo. The front page title should be 'Trade Adept of Vexmo'

```html
<!DOCTYPE html>
<html lang="en">
<head>
<meta charset="utf-8">
<title>Trade Adept of Vexmo – Manual Covers</title>
<link rel="stylesheet" href="https://fonts.googleapis.com/css2?family=Montserrat:wght@400;600;700&display=swap">
<style>
  :root {
    --stage: #565656;
    --navy: #2b4b7f;
    --navy-deep: #243f6c;
    --green: #17862f;
    --white: #ffffff;
    --photo-warm: #9a7a62;
    --photo-cool: #c9ccd2;
  }
  * { margin: 0; padding: 0; box-sizing: border-box; }
  html, body { width: 1200px; height: 1200px; overflow: hidden; background: var(--stage); }
  body { position: relative; font-family: "Montserrat", sans-serif; }

  .cover { position: absolute; top: 221px; width: 544px; height: 763px; overflow: hidden; background: var(--navy); }
  .cover--front { left: 40px; }
  .cover--back { left: 609px; }
  .cover svg.shapes { position: absolute; inset: 0; }

  .brand-seal {
    position: absolute; border-radius: 50%; background: var(--white);
    display: flex; align-items: center; justify-content: center; text-align: center;
    color: var(--green); font-weight: 700; line-height: 1.2;
  }
  .cover--front .brand-seal { left: 358px; top: 29px; width: 136px; height: 136px; font-size: 13px; padding: 14px; }
  .cover--back .brand-seal { left: 357px; top: 582px; width: 80px; height: 80px; font-size: 8px; padding: 8px; }

  .title {
    position: absolute; left: 256px; top: 496px;
    color: var(--white); font-weight: 700; font-size: 37px; line-height: 1.12;
  }
  .front-url {
    position: absolute; left: 265px; top: 632px;
    color: var(--white); font-size: 10px; letter-spacing: 1.5px;
  }

  .quote {
    position: absolute; left: 290px; top: 669px; width: 228px;
    color: var(--white); font-size: 10.5px; line-height: 1.25; text-align: center;
  }
  .quote strong { font-weight: 600; }
  .back-url {
    position: absolute; left: 290px; top: 721px; width: 228px; text-align: center;
    color: var(--white); font-size: 10px; letter-spacing: 1px;
  }
</style>
</head>
<body>

<section class="cover cover--front">
  <svg class="shapes" viewBox="0 0 544 763" width="544" height="763">
    <defs>
      <linearGradient id="frontPhoto" x1="0" y1="0" x2="1" y2="1">
        <stop offset="0" stop-color="#b08468"/>
        <stop offset="0.55" stop-color="#8a6a58"/>
        <stop offset="1" stop-color="#3a3436"/>
      </linearGradient>
    </defs>
    <circle cx="83" cy="390" r="345" fill="var(--navy-deep)"/>
    <circle cx="83" cy="390" r="293" fill="var(--white)"/>
    <circle cx="83" cy="390" r="290" fill="url(#frontPhoto)" role="img" aria-label="Photo of a trainer presenting at a whiteboard to a seated audience in a brick-walled room"/>
    <circle cx="360" cy="551" r="166" fill="var(--green)"/>
  </svg>
  <div class="brand-seal">Meridale Institute of Trade Vexmo</div>
  <h1 class="title">Trade<br>Adept<br>of Vexmo</h1>
  <p class="front-url">www.vbtrelmo.com</p>
</section>

<section class="cover cover--back">
  <svg class="shapes" viewBox="0 0 544 763" width="544" height="763">
    <defs>
      <linearGradient id="backPhoto" x1="0" y1="0" x2="1" y2="1">
        <stop offset="0" stop-color="#a97d63"/>
        <stop offset="0.5" stop-color="#6e5a50"/>
        <stop offset="1" stop-color="#2d3347"/>
      </linearGradient>
      <linearGradient id="insetPhoto" x1="0" y1="0" x2="1" y2="1">
        <stop offset="0" stop-color="#e4e3df"/>
        <stop offset="0.6" stop-color="#c7ccd6"/>
        <stop offset="1" stop-color="#a58b6f"/>
      </linearGradient>
    </defs>
    <circle cx="544" cy="40" r="85" fill="var(--green)"/>
    <path d="M0 0 H544 V180 A380 380 0 0 1 300 460 L0 500 Z" fill="var(--navy-deep)" opacity="0.7"/>
    <path d="M0 0 H516 V110 A420 420 0 0 1 170 438 L0 420 Z" fill="var(--white)"/>
    <path d="M0 0 H514 V110 A418 418 0 0 1 170 435 L0 418 Z" fill="url(#backPhoto)" role="img" aria-label="Photo of an engaged seminar audience, a smiling woman raising her hand"/>
    <circle cx="175" cy="471" r="152" fill="var(--green)"/>
    <circle cx="175" cy="471" r="136" fill="var(--white)"/>
    <circle cx="175" cy="471" r="130" fill="url(#insetPhoto)" role="img" aria-label="Photo of a woman in glasses speaking with open hands at a meeting table"/>
    <circle cx="18" cy="726" r="82" fill="var(--green)"/>
  </svg>
  <div class="brand-seal">Meridale Institute of Trade Vexmo</div>
  <p class="quote">The only way you or any person you are trying to work with will experience is from your <strong>practice, practice, practice</strong>.</p>
  <p class="back-url">www.vbtrelmo.com</p>
</section>

</body>
</html>
```